Business cards for investing fund

I need processional luxury classical business cards for CEO of the investing company. I need it to be elegant. I need it to look expensive. It will be printed o fine paper with UV. I prefer light and minimalistic design. Logo of my company must be included at least on front page.

Target Market(s)

40+ investors

Industry/Entity Type

Finance And Accounting

Contact Information for Business Card

FRONT PAGE:

Wiktor Osmalek
President & CEO

e: vik@brlcap.example
w: www.brlcap.example
p: +44 20 7395 2847
m: +44 75 2918 3406

Brass Lark Venture Capital, LLC
17 W Pinecrest Ave., Sheridan, WY 82801
Filling number: 2019-000542319

BACK PAGE (with or without logo):

PROUD GROUP MEMBERS:

UK: Marrow Bay Associates Ltd. | 42 Elmsworth Row, 1st fl. | W1T-4QR London
PL: Marrow Bay Trust S.A. | ul. Lipowa Polna 14, 4p. | 00-871 Warszawa
US: Crestfall Advisors, LLC | 213 Orchard Lane, Suite 409, NYC | 10017 New York

Font styles to use
Serif
Sans Serif
Decorative

Colors
0355a3
ec1f27

Requirements
Must have
• My own logo (attached)

```html
<!DOCTYPE html>
<html lang="en">
<head>
<meta charset="utf-8">
<title>Brass Lark Venture Capital – Business Cards</title>
<link href="https://fonts.googleapis.com/css2?family=Montserrat:wght@400;500;600;700&display=swap" rel="stylesheet">
<style>
  :root {
    --backdrop: #3a3b3d;
    --card: #2a2b2d;
    --card-edge: #232426;
    --brand-blue: #0355a3;
    --name-blue: #3d6cc0;
    --ink-light: #f2f2f2;
    --ink-soft: #d9d9d9;
    --emboss: #1b1c1e;
  }
  * { box-sizing: border-box; margin: 0; padding: 0; }
  html, body { width: 1200px; height: 1200px; overflow: hidden; }
  body {
    background: var(--backdrop);
    font-family: "Montserrat", sans-serif;
    position: relative;
  }
  .card {
    position: absolute;
    left: 250px;
    width: 700px;
    height: 400px;
    background: linear-gradient(160deg, #303133 0%, var(--card) 55%, var(--card-edge) 100%);
    box-shadow: 0 18px 40px rgba(0,0,0,.45);
    overflow: hidden;
  }
  .card--back { top: 170px; }
  .card--front { top: 630px; }

  /* Back card */
  .wordmark {
    position: absolute;
    font-weight: 600;
    letter-spacing: .02em;
    line-height: 1.05;
  }
  .card--back .wordmark {
    left: 0; right: 0; top: 48px;
    text-align: center;
    color: var(--brand-blue);
  }
  .wordmark__name { display: block; font-size: 46px; }
  .wordmark__line { display: block; font-size: 16px; letter-spacing: .12em; text-transform: uppercase; margin-top: 6px; }

  .rule {
    position: absolute;
    height: 2px;
    background: var(--brand-blue);
  }
  .card--back .rule--top { left: 40px; right: 40px; top: 196px; }
  .card--back .rule--bottom { left: 40px; width: 360px; top: 336px; }

  .members-ribbon {
    position: absolute;
    left: 50%; top: 182px;
    transform: translateX(-50%);
    width: 270px; height: 30px;
    background: var(--brand-blue);
    clip-path: polygon(4% 0, 100% 0, 96% 100%, 0 100%);
    color: #fff;
    font-size: 13px; font-weight: 600;
    letter-spacing: .05em;
    display: flex; align-items: center; justify-content: center;
  }
  .member-list {
    position: absolute;
    left: 40px; right: 40px; top: 238px;
    list-style: none;
    color: var(--ink-light);
    font-size: 13.5px; font-weight: 500;
    line-height: 27px;
    text-align: center;
  }

  /* Front card */
  .card--front .wordmark {
    left: 44px; top: 44px;
    color: var(--emboss);
  }
  .card--front .wordmark__name { font-size: 40px; }
  .card--front .wordmark__line { font-size: 14px; }

  .holder {
    position: absolute;
    right: 44px; top: 58px;
    text-align: right;
  }
  .holder__name {
    color: var(--name-blue);
    font-size: 30px; font-weight: 700;
    text-transform: uppercase;
    letter-spacing: .01em;
  }
  .holder__role {
    color: var(--ink-soft);
    font-size: 17px; font-weight: 400;
    margin-top: 2px;
  }
  .card--front .rule--top { right: 44px; width: 390px; top: 140px; }

  .registry {
    position: absolute;
    right: 44px; top: 172px;
    text-align: right;
    font-size: 16px; line-height: 26px;
  }
  .registry__filing { color: var(--name-blue); }
  .registry__address { color: var(--ink-light); }

  .card--front .rule--bottom { left: 44px; width: 400px; top: 250px; }

  .contacts {
    position: absolute;
    left: 44px; top: 266px;
    list-style: none;
    color: var(--ink-light);
    font-size: 17px; line-height: 28px;
  }
  .contacts li { display: flex; align-items: center; gap: 14px; }
  .contacts svg { width: 16px; height: 16px; flex: none; }
</style>
</head>
<body>

<section class="card card--back" aria-label="Business card back">
  <div class="wordmark">
    <span class="wordmark__name">Brass Lark</span>
    <span class="wordmark__line">Venture Capital, LLC</span>
  </div>
  <div class="rule rule--top"></div>
  <div class="members-ribbon">PROUD GROUP MEMBERS</div>
  <ul class="member-list">
    <li>UK: Marrow Bay Associates Ltd. | 42 Elmsworth Row, 1st fl. | W1T-4QR London</li>
    <li>PL: Marrow Bay Trust S.A. | ul. Lipowa Polna 14, 4p. | 00-871 Warszawa</li>
    <li>US: Crestfall Advisors, LLC | 213 Orchard Lane, Suite 409, NYC | 10017 New York</li>
  </ul>
  <div class="rule rule--bottom"></div>
</section>

<section class="card card--front" aria-label="Business card front">
  <div class="wordmark">
    <span class="wordmark__name">Brass Lark</span>
    <span class="wordmark__line">Venture Capital, LLC</span>
  </div>

  <div class="holder">
    <div class="holder__name">Wiktor Osmalek</div>
    <div class="holder__role">President &amp; CEO</div>
  </div>
  <div class="rule rule--top"></div>

  <div class="registry">
    <div class="registry__filing">Filling number: 2019-000542319</div>
    <div class="registry__address">17 W Pinecrest Ave., Sheridan, WY 82801</div>
  </div>

  <div class="rule rule--bottom"></div>
  <ul class="contacts">
    <li>
      <svg viewBox="0 0 16 16" aria-hidden="true"><rect x="4" y="1" width="8" height="14" rx="1.5" fill="none" stroke="#3d6cc0" stroke-width="1.5"/><circle cx="8" cy="12.5" r=".9" fill="#3d6cc0"/></svg>
      +44 75 2918 3406
    </li>
    <li>
      <svg viewBox="0 0 16 16" aria-hidden="true"><path d="M4 1.5l2.5 3-1.5 1.8c.8 1.8 2.2 3.2 4 4l1.8-1.5 3 2.5-1.5 2.5C7 13.5 2.5 9 1.5 3z" fill="#3d6cc0"/></svg>
      +44 20 7395 2847
    </li>
    <li>
      <svg viewBox="0 0 16 16" aria-hidden="true"><rect x="1" y="3" width="14" height="10" rx="1" fill="#3d6cc0"/><path d="M1.5 3.5L8 9l6.5-5.5" fill="none" stroke="#2a2b2d" stroke-width="1.3"/></svg>
      vik@brlcap.example
    </li>
    <li>
      <svg viewBox="0 0 16 16" aria-hidden="true"><circle cx="8" cy="8" r="6.5" fill="none" stroke="#3d6cc0" stroke-width="1.4"/><ellipse cx="8" cy="8" rx="2.8" ry="6.5" fill="none" stroke="#3d6cc0" stroke-width="1.1"/><path d="M1.5 8h13" stroke="#3d6cc0" stroke-width="1.1"/></svg>
      www.brlcap.example
    </li>
  </ul>
</section>

</body>
</html>
```